Lomi Lomi Business
Zielgruppe
Lomi Lomi Massage /Wellnessmassage
Aufgabenstellung
Design, Farbgebung und Maße bitte angelehnt an das Velkaro-Design #22
Format 10,5x21cm Querformat (DIN Lang plus beim Anbieter "Prospektwelle" genannt)
Texte siehe Anhang
Daten bitte in editierbarem Illustrator, oder InDesign-Format

```html
<!DOCTYPE html>
<html lang="de">
<head>
<meta charset="utf-8">
<title>Jonas Veltmann – Hawaiianische Massage &amp; Körperarbeit</title>
<link href="https://fonts.googleapis.com/css2?family=Maven+Pro:wght@400;500;700;800&display=swap" rel="stylesheet">
<style>
:root{
  --page:#dcdadb;
  --slate:#565455;
  --leaf:#5b8a0c;
  --cream:#fddba1;
  --white:#ffffff;
  --ink-green:#4d7a08;
}
*{margin:0;padding:0;box-sizing:border-box}
html,body{width:848px;height:1200px;overflow:hidden}
body{background:var(--page);font-family:"Maven Pro",sans-serif;position:relative}
.flyer{position:absolute;left:28px;width:787px;height:393px;overflow:hidden;box-shadow:3px 3px 4px rgba(0,0,0,.35)}
.flyer--front{top:72px;background:var(--slate)}
.flyer--back{top:568px;background:var(--white)}
.flyer svg.backdrop{position:absolute;inset:0}
.t{position:absolute;white-space:nowrap}

/* front */
.brand{left:22px;top:18px;font-size:21px;line-height:26.5px;letter-spacing:1.3px}
.brand .name{color:var(--white)}
.brand .kind{color:var(--cream)}
.brand .craft{color:var(--leaf)}
.stamp{position:absolute;left:83px;top:121px;width:190px;height:150px;z-index:1}
.offer{position:absolute;left:28px;top:202px;width:316px;height:54px;transform:rotate(-5deg);z-index:2;
  background:var(--slate);border:2px solid var(--leaf);
  display:flex;flex-direction:column;align-items:center;justify-content:center;
  color:var(--cream);font-weight:800;font-size:16px;line-height:19px;letter-spacing:.6px;
  text-shadow:1px 1px 0 var(--ink-green),-1px 0 0 var(--ink-green),0 -1px 0 var(--ink-green)}
.prices{left:23px;top:283px;font-size:11.2px;line-height:13.4px;letter-spacing:1px;color:var(--white)}
.prices h3{color:var(--leaf);font-size:11px;font-weight:700;margin-bottom:13px}
.prices .item{color:var(--cream)}
.prices p{margin-bottom:13px}

/* back */
.about{font-size:10.2px;line-height:12.7px;color:var(--leaf);letter-spacing:.2px}
.about b{font-weight:700}
.about--one{left:29px;top:20px}
.about--two{left:86px;top:82px}
.about--three{left:30px;top:166px}
.contact{left:525px;top:35px;font-size:11.2px;line-height:13.2px;letter-spacing:.7px;color:var(--white)}
.contact h3{color:var(--leaf);font-size:11px;font-weight:700;margin-bottom:13px}
.contact .kind{color:var(--cream)}
.contact .craft{color:var(--leaf)}
.contact .gap{height:13px}
.portrait{position:absolute;left:396px;top:229px;width:102px;height:144px;border:2px solid var(--cream);
  background:linear-gradient(180deg,#e6c48a 0%,#d9b27a 55%,#2a2a2a 80%,#1d1d1d 100%)}
.bio{left:526px;top:304px;font-size:11.2px;line-height:13.2px;letter-spacing:.6px;color:var(--cream)}
.bio .name{color:var(--white)}
</style>
</head>
<body>

<section class="flyer flyer--front">
  <svg class="backdrop" width="787" height="393" viewBox="0 0 787 393">
    <defs>
      <linearGradient id="skin" x1="0" y1="0" x2="1" y2="1">
        <stop offset="0" stop-color="#e9dcd8"/>
        <stop offset=".35" stop-color="#c97a52"/>
        <stop offset=".7" stop-color="#a8583a"/>
        <stop offset="1" stop-color="#e8e2de"/>
      </linearGradient>
    </defs>
    <rect class="photo" x="0" y="0" width="787" height="393" fill="url(#skin)" role="img" aria-label="Foto: entspannte Frau erhält eine Rückenmassage"/>
    <path fill="var(--leaf)" d="M362 0 C318 32 312 98 352 168 C396 242 456 300 398 393 H0 V0Z"/>
    <path fill="var(--cream)" d="M352 0 C306 32 300 98 340 168 C384 244 440 300 380 393 H0 V0Z"/>
    <path fill="var(--slate)" d="M344 0 C298 32 292 98 332 168 C374 244 426 300 368 393 H0 V0Z"/>
  </svg>

  <div class="t brand">
    <div class="name">Jonas Veltmann</div>
    <div class="kind">Hawaiianische</div>
    <div class="craft">Massage &amp; Körperarbeit</div>
  </div>

  <svg class="stamp" viewBox="0 0 190 150" aria-label="Praxiseröffnung">
    <defs><path id="arc" d="M38 75 A57 57 0 0 1 152 75"/></defs>
    <circle cx="95" cy="75" r="72" fill="var(--leaf)"/>
    <circle cx="95" cy="75" r="63" fill="none" stroke="var(--white)" stroke-width="2"/>
    <text font-family="Maven Pro, sans-serif" font-weight="800" font-size="12" fill="var(--white)" letter-spacing="1.5">
      <textPath href="#arc" startOffset="50%" text-anchor="middle">PRAXISERÖFFNUNG</textPath>
    </text>
  </svg>

  <div class="offer">
    <span>Erhalten Sie Ihre erste Massage</span>
    <span>zum halben Preis!</span>
  </div>

  <div class="t prices">
    <h3>Preise:</h3>
    <p><span class="item">Lomi-Lomi Massage (90 Minuten)</span> 95Euro<br>(Lomi Ganzkörpermassage – Gesamtdauer ca.2 Std.)</p>
    <p><span class="item">Business-Massage (30 Minuten)</span> 35 Euro<br>(z.B. für die Mittagspause – Gesamtdauer ca.45Min)</p>
  </div>
</section>

<section class="flyer flyer--back">
  <svg class="backdrop" width="787" height="393" viewBox="0 0 787 393">
    <defs>
      <radialGradient id="leaves" cx=".45" cy=".6" r=".6">
        <stop offset="0" stop-color="#6fae2c"/>
        <stop offset=".6" stop-color="#8cc44a" stop-opacity=".8"/>
        <stop offset="1" stop-color="#ffffff" stop-opacity="0"/>
      </radialGradient>
    </defs>
    <circle cx="43" cy="43" r="31" fill="var(--cream)"/>
    <circle cx="106" cy="112" r="46" fill="var(--cream)"/>
    <circle cx="42" cy="195" r="39" fill="var(--cream)"/>
    <rect x="0" y="225" width="400" height="168" fill="url(#leaves)" role="img" aria-label="Illustration: grüne Bambusstange mit Blättern"/>
    <path fill="var(--leaf)" d="M446 0 C470 40 476 110 448 170 C420 230 372 280 384 393 H787 V0Z"/>
    <path fill="var(--cream)" d="M458 0 C482 40 488 110 460 170 C432 230 386 280 400 393 H787 V0Z"/>
    <path fill="var(--slate)" d="M466 0 C490 40 496 110 468 170 C440 230 396 280 410 393 H787 V0Z"/>
  </svg>

  <div class="t about about--one"><b>Die hawaiianische Lomi Lomi Massage</b> (oder Tempelmassage)<br>ist eine Berührungskunst, welche von den Kahunas – den Wissensträgern – bis heute<br>praktiziert und weitergegeben wird.</div>
  <div class="t about about--two"><b>In der Massage wird der gesamte Körper</b> unter Verwendung von<br>hochwertigem Massageöl mit Handballen und Unterarmen in<br>langen, fließenden Bewegungen massiert und ausgestrichen.<br>Dadurch kann die Behandlung  zu einer tiefen Entspannung führen<br>und Stress abbauen.</div>
  <div class="t about about--three"><b>Die Intensität und den Charakter der Massage</b> bestimmen<br>dabei der Körper des Klienten und das Wesen des Moments.<br>Der Intimbereich bleibt dabei stets<br>abgedeckt und unberührt.</div>

  <div class="t contact">
    <h3>Kontakt:</h3>
    <div>Jonas Veltmann</div>
    <div><span class="kind">Hawaiianische</span> <span class="craft">Massage &amp; Körperarbeit</span></div>
    <div>Lindenhöfchen 7, 96052 Auerbach</div>
    <div>( Eingang „Die Wohlfühlerei“)</div>
    <div class="gap"></div>
    <div>Telefon  0951-480 372 55</div>
    <div class="gap"></div><div class="gap"></div>
    <div>Termine nach Vereinbarung</div>
  </div>

  <div class="portrait" role="img" aria-label="Porträtfoto des Masseurs"></div>

  <div class="t bio">
    <div class="name">Jonas Veltmann – Jahrgang 1979</div>
    <div>Lomi Lomi Practitioner</div>
    <div>(nach Kahu Makani von Hanalei)</div>
    <div>Romi-Kahuna-Bodywork Practitioner</div>
    <div>Wellnessmasseur &amp; Wellnesstherapeut</div>
  </div>
</section>

</body>
</html>
```